Paw Summit Co business card

I need a business card design for a dog training company in Toronto called Paw Summit Co. My training is unique, outdoor training that helps people create a better bond with their dog through communication and understanding their dog's true nature. I do not use treats - but communication and praise for the dog.

I help people create a better life for them and their dog. From puppy training right through to seniors, I offer both group classes called Curbside Poise Course as well as in-home private sessions.

I believe that having a dog is a lifestyle, so I encourage clients to incorporate their dog into their active life. Outdoor activities such as hiking, mental stimulation, proper care and healthy food for their dog are all keys to a healthy and happy dog.

I would like a fresh and modern look that works with my logo. I would like to convey fun, confidence and happiness.

My services are premium services. I am a Certified Dog Trainer, and offer value for money, but my prices are higher than other trainers.
Updates

Thank you to everyone who submitted designs! I'm so impressed with the level of creativity and the options that you all have given me. It will be a difficult choice for sure. As this was my first experience with Art Huddle - it has been a great one.

maren.

Industry/Entity Type

Communication

Requirements
Must have
• Maren Quill, CTE
Certified Trainer Educator
maren@pawsummitco.ca
555-318-0472
pawsummitco.ca

Prefer a double sided card.
Must have Paw Summit Co logo. File attached. I do have a stroke logo for a dark background as well.

Must only use the fonts and colours as outlined in my brand guidelines, which are attached.
Should not have
• no cheesy pet images
do not use the tongue as an element outside of the logo
minimize the use of pink - can be used as an accent colour but should not be a main colour

```html
<!DOCTYPE html>
<html lang="en">
<head>
<meta charset="utf-8">
<title>Paw Summit Co — Business Card</title>
<link href="https://fonts.googleapis.com/css2?family=Josefin+Sans:wght@300;400&family=Jost:wght@300;400;500;600&display=swap" rel="stylesheet">
<style>
  :root {
    --page: #ffffff;
    --card-light: #f3f4f6;
    --card-edge: #7a7a7a;
    --brand-green: #9bbb50;
    --charcoal: #414143;
    --label: #5a5a5a;
  }
  html, body {
    margin: 0;
    padding: 0;
    width: 1200px;
    height: 848px;
    overflow: hidden;
    background: var(--page);
  }
  .sheet {
    position: relative;
    width: 1200px;
    height: 848px;
    font-family: "Jost", sans-serif;
  }
  .card {
    position: absolute;
    top: 169px;
    height: 497px;
    box-sizing: border-box;
  }
  .card--front {
    left: 202px;
    width: 344px;
    background: var(--card-light);
    border: 1px solid var(--card-edge);
  }
  .card--back {
    left: 677px;
    width: 338px;
    background: var(--charcoal);
  }
  .front__band {
    position: absolute;
    top: 0;
    right: 0;
    width: 91px;
    height: 100%;
    background: var(--brand-green);
  }
  .back__band {
    position: absolute;
    top: 0;
    left: 0;
    width: 87px;
    height: 100%;
    background: var(--brand-green);
  }
  .brand-name {
    position: absolute;
    left: 22px;
    top: 245px;
    transform: translateY(-160px);
    margin: 0;
    width: 220px;
    font-family: "Jost", sans-serif;
    font-weight: 600;
    font-size: 40px;
    line-height: 40px;
    color: var(--charcoal);
  }
  .holder {
    position: absolute;
    left: 22px;
    top: 300px;
  }
  .holder__name {
    margin: 0;
    font-weight: 600;
    font-size: 21px;
    color: var(--charcoal);
  }
  .holder__title {
    margin: 6px 0 0;
    font-weight: 300;
    font-size: 16px;
    color: var(--label);
  }
  .divider {
    position: absolute;
    left: 20px;
    top: 382px;
    width: 232px;
    height: 3px;
    background: var(--brand-green);
  }
  .contact {
    position: absolute;
    left: 22px;
    top: 402px;
    margin: 0;
    padding: 0;
    list-style: none;
    font-weight: 300;
    font-size: 15px;
    line-height: 22px;
    color: var(--charcoal);
  }
  .side-label {
    position: absolute;
    top: 670px;
    margin: 0;
    font-family: "Josefin Sans", sans-serif;
    font-weight: 300;
    font-size: 38px;
    color: var(--label);
    transform: translateX(-50%);
  }
  .side-label--front { left: 354px; }
  .side-label--back { left: 866px; }
</style>
</head>
<body>
<main class="sheet">
  <section class="card card--front" aria-label="Card front">
    <div class="front__band"></div>
    <h1 class="brand-name">Paw Summit Co</h1>
    <div class="holder">
      <p class="holder__name">Maren Quill, CTE</p>
      <p class="holder__title">Certified Trainer Educator</p>
    </div>
    <div class="divider"></div>
    <ul class="contact">
      <li>maren@pawsummitco.ca</li>
      <li>555-318-0472</li>
      <li>pawsummitco.ca</li>
    </ul>
  </section>
  <p class="side-label side-label--front">front</p>

  <section class="card card--back" aria-label="Card back">
    <div class="back__band"></div>
  </section>
  <p class="side-label side-label--back">back</p>
</main>
</body>
</html>
```